Edit of flyers - text to be eddited

I currently have three flyers already designed, but want to edit the text on them. On the front of each flyer I want to delete the text which states: "50% off lawn mowing applies to first lawn mowed on any regular service and applies to first 100 callers so call now" and replace it with "Professional Lawn and Garden Maintenance".

Also on the front and rear of each flyer I want to replace the text which states "Leo and Martin" with "Martin Hollis."

All other details can stay the same thanks. I need each of the files saved as a pdf according to the instructions attached with the bleed area set as specified for printing.

Font styles to use
Serif

Colors
acd036
fbed22

Requirements
Must have
• On the front of each flyer I want to delete the text which states: "50% off lawn mowing applies to first lawn mowed on any regular service and applies to first 100 callers so call now" and replace it with "Professional Lawn and Garden Maintenance".
• Also on the front and rear of each flyer I want to replace the text which states "Leo and Martin" with "Martin Hollis."
• All other details can stay the same thanks. I need each of the files saved as a pdf according to the instructions attached with the bleed area set as specified for printing.

```html
<!DOCTYPE html>
<html lang="en">
<head>
<meta charset="utf-8">
<title>Meadowline Lawns – Flyer</title>
<link href="https://fonts.googleapis.com/css2?family=Lobster&family=Montserrat:wght@700&family=PT+Sans:wght@700&display=swap" rel="stylesheet">
<style>
  :root {
    --brand-green: #0f6a3a;
    --leaf-green: #1c9a4c;
    --stripe-green: #6cbf4a;
    --orange: #f09a35;
    --white: #ffffff;
    --sky-top: #f3a93c;
    --sky-mid: #f9df72;
    --field-light: #b9d84a;
    --field-dark: #4f962a;
  }
  html, body {
    margin: 0;
    padding: 0;
    overflow: hidden;
    background: var(--white);
  }
  .flyer {
    position: relative;
    width: 1200px;
    height: 598px;
    overflow: hidden;
    background: var(--white);
  }
  .brand-panel {
    position: absolute;
    left: 0;
    top: 0;
    width: 388px;
    height: 598px;
    background: var(--white);
  }
  .brand-name {
    position: absolute;
    left: 0;
    width: 388px;
    top: 222px;
    text-align: center;
    font-family: "Lobster", cursive;
    font-size: 38px;
    color: var(--leaf-green);
    margin: 0;
    font-weight: 400;
  }
  .brand-tagline {
    position: absolute;
    left: 0;
    width: 388px;
    top: 390px;
    text-align: center;
    font-family: "Lobster", cursive;
    font-size: 25px;
    color: var(--leaf-green);
    margin: 0;
  }
  .divider {
    position: absolute;
    left: 386px;
    top: 0;
    width: 5px;
    height: 598px;
    background: var(--stripe-green);
  }
  .field-photo {
    position: absolute;
    left: 391px;
    top: 0;
    width: 809px;
    height: 598px;
    background:
      radial-gradient(circle at 88% 18%, rgba(255,255,230,0.95) 0, rgba(255,240,170,0.6) 90px, rgba(255,230,140,0) 260px),
      linear-gradient(to bottom, var(--sky-top) 0%, var(--sky-mid) 24%, var(--field-light) 36%, #8ec23a 60%, var(--field-dark) 100%);
  }
  .headline {
    position: absolute;
    left: 391px;
    width: 770px;
    top: 128px;
    margin: 0;
    text-align: center;
    font-family: "Lobster", cursive;
    font-weight: 400;
    font-size: 60px;
    line-height: 88px;
    color: var(--brand-green);
    -webkit-text-stroke: 6px var(--white);
    paint-order: stroke fill;
    text-shadow: 0 0 10px rgba(255,255,255,0.6);
  }
  .offer {
    position: absolute;
    left: 448px;
    top: 348px;
    margin: 0;
    font-family: "Montserrat", sans-serif;
    font-weight: 700;
    font-size: 39px;
    line-height: 50px;
    color: var(--orange);
    -webkit-text-stroke: 5px var(--white);
    paint-order: stroke fill;
  }
  .contact {
    position: absolute;
    right: 28px;
    top: 460px;
    margin: 0;
    text-align: right;
    font-family: "PT Sans", sans-serif;
    font-weight: 700;
    font-size: 21px;
    line-height: 29px;
    color: var(--brand-green);
    -webkit-text-stroke: 4px var(--white);
    paint-order: stroke fill;
    font-style: normal;
  }
  .contact span { display: block; }
</style>
</head>
<body>
  <main class="flyer">
    <section class="brand-panel">
      <h2 class="brand-name">Meadowline Lawns</h2>
      <p class="brand-tagline">Lawn and Garden Maintenance</p>
    </section>
    <div class="divider"></div>
    <div class="field-photo" role="img" aria-label="Sunlit green meadow with yellow wildflowers under a golden sky"></div>
    <h1 class="headline">Professional Lawn and<br>Garden Maintenance</h1>
    <p class="offer">Professional lawn mowing<br>at an affordable price.</p>
    <address class="contact">
      <span>Martin Hollis</span>
      <span>Ph: 0400555018</span>
      <span>Email: hello@meadowlinelawns.com</span>
      <span>www.meadowlinelawns.com.au</span>
    </address>
  </main>
</body>
</html>
```